Micropayment solution needs a Wordpress Design

We need a wordpress design for a new company based in London. Micropayment and mobile payment technologies. Varnel, Quorvath, Fembrisk payments.
We need a one page website design.

If you have any question, please don't hesitate to contact us.

Industry/Entity Type

It Company

Font styles to use
Other font styles liked:
• Maven Pro

Requirements
Must have
• We need a clean and user friendly interface.
Should not have
• we don't wanna to see rounded pages.

```html
<!DOCTYPE html>
<html lang="en">
<head>
<meta charset="utf-8">
<title>Pennimo Pay</title>
<link rel="stylesheet" href="https://fonts.googleapis.com/css2?family=Maven+Pro:wght@400;500;700&display=swap">
<style>
:root{
  --red:#d0202a;
  --charcoal:#4a4a4a;
  --ink:#333;
  --text:#555;
  --muted:#888;
  --tile-grey:#d6d6d6;
  --tile-white:#fff;
  --line:#e2e2e2;
  --footer:#2f2f2f;
  --footer-bottom:#222;
}
*{margin:0;padding:0;box-sizing:border-box}
html,body{width:1200px;height:2413px;overflow:hidden}
body{font-family:"Maven Pro",Arial,sans-serif;color:var(--text);background:#fff;position:relative}

/* header */
.site-header{position:absolute;left:0;top:0;width:1200px;height:98px;background:var(--red);color:#fff}
.brand{position:absolute;left:161px;top:40px;font-size:16px;font-weight:700;letter-spacing:.5px}
.call{position:absolute;left:828px;top:22px;display:flex;align-items:center;gap:12px;font-size:14px;letter-spacing:.6px}
.call .dot{width:30px;height:30px;border-radius:50%;background:#fff;display:flex;align-items:center;justify-content:center}
.main-nav{position:absolute;left:499px;top:71px;display:flex;gap:26px;font-size:11px;letter-spacing:.3px}
.main-nav a{color:#fff;text-decoration:none;position:relative}
.main-nav .u{text-decoration:underline}
.main-nav .active::after{content:"";position:absolute;left:-4px;right:-4px;top:24px;height:2px;background:#fff}
.main-nav .active::before{content:"";position:absolute;left:50%;top:20px;width:9px;height:9px;margin-left:-4px;border-radius:50%;background:#fff}

/* hero */
.hero{position:absolute;left:0;top:98px;width:1200px;height:462px;
  background:linear-gradient(180deg,#1c3b52 0%,#2d4b5c 45%,#3a3a3e 70%,#5a4a3c 85%,#2a3440 100%)}
.hero h1{position:absolute;left:0;width:1200px;top:150px;text-align:center;color:#fff;font-size:46px;font-weight:500;letter-spacing:1px}
.hero p{position:absolute;left:330px;width:540px;top:224px;text-align:center;color:#fff;font-size:16px;line-height:26px}
.hero-arrow{position:absolute;top:202px;width:54px;height:54px;border:2px solid rgba(255,255,255,.75);border-radius:50%;background:rgba(255,255,255,.12)}
.hero-arrow.prev{left:24px}.hero-arrow.next{left:1112px}
.hero-arrow svg{position:absolute;left:17px;top:15px}

/* feature cards */
.feature{position:absolute;background:#fff;border:1px solid #e6e6e6;text-align:center;box-shadow:0 0 6px rgba(0,0,0,.08)}
.feature .icon{width:72px;height:72px;border:2px solid var(--red);border-radius:50%;margin:0 auto;display:flex;align-items:center;justify-content:center}
.feature h3{font-size:14px;font-weight:500;color:var(--ink);letter-spacing:.5px;margin-top:18px}
.feature p{font-size:10.5px;line-height:21px;color:var(--muted);padding:0 26px;margin-top:14px}
.btn{display:inline-block;background:var(--red);color:#fff;font-size:10.5px;font-weight:700;padding:11px 22px;letter-spacing:.2px;box-shadow:0 2px 3px rgba(0,0,0,.2)}
.coins{display:flex;gap:8px;justify-content:center;margin-top:14px}
.coins span{width:78px;height:50px;border:1px solid #ddd;display:flex;align-items:center;justify-content:center;font-size:11px;color:var(--ink)}
.ticks{list-style:none;text-align:left;padding:0 20px;margin-top:12px}
.ticks li{font-size:10px;line-height:20px;color:var(--text);display:flex;align-items:center;gap:8px}
.ticks li::before{content:"";width:8px;height:8px;border-radius:50%;background:var(--red);flex:none}
.ticks a{color:var(--red);text-decoration:none}

/* integrations */
.integrations{position:absolute;left:0;top:881px;width:1200px;height:847px;
  background:linear-gradient(180deg,#3a3530 0%,#4a4038 35%,#2e2e30 70%,#1c1c1e 100%)}
.section-title{position:absolute;left:0;width:1200px;text-align:center;font-size:22px;letter-spacing:1px;font-weight:400}
.section-title .star{font-size:14px;letter-spacing:2px;margin:0 10px;vertical-align:3px}
.coin-strip{position:absolute;left:336px;top:91px;width:526px;height:119px;display:flex}
.coin-strip div{flex:1;display:flex;align-items:center;justify-content:center;font-size:24px;font-weight:700;color:#333}
.coin-strip div:nth-child(odd){background:#e4e4e4}
.coin-strip div:nth-child(2){background:#fff}
.coin-strip i{width:22px;height:22px;border-radius:50%;background:#f0a020;margin-right:8px;display:inline-block}
.group{position:absolute;width:293px;height:246px;background:#ececec}
.group .bar{height:43px;display:flex;align-items:center;justify-content:space-between;padding:0 10px;color:#fff;font-size:14px;letter-spacing:.4px}
.group .bar.red{background:var(--red)}
.group .bar.dark{background:var(--charcoal)}
.group .bar b{font-weight:400;font-size:14px;opacity:.8}
.tiles{display:grid;grid-template-columns:137px 137px;gap:6px;padding:6px 6px}
.tiles span{height:88px;display:flex;align-items:center;justify-content:center;font-size:15px;font-weight:500;color:#3a3a3a}
.tiles .g{background:var(--tile-grey)}
.tiles .w{background:var(--tile-white)}
.pos-notes{list-style:none;padding:10px 12px 0}
.pos-notes li{font-size:10px;line-height:17px;color:var(--text);display:flex;gap:8px;margin-bottom:10px}
.pos-notes li::before{content:"";width:8px;height:8px;border-radius:50%;background:var(--red);flex:none;margin-top:4px}

/* pricing */
.plan{position:absolute;top:1805px;width:273px;height:193px;color:#fff;text-align:center}
.plan.red{background:var(--red)}
.plan.dark{background:var(--charcoal)}
.plan h4{font-size:15px;font-weight:500;letter-spacing:.5px;margin-top:28px}
.plan ul{list-style:none;margin-top:18px}
.plan li{font-size:10px;line-height:28px}
.plan li::before{content:"";display:inline-block;width:7px;height:7px;border-radius:50%;background:#fff;margin-right:6px}
.plan .fold{position:absolute;right:0;bottom:0}
.divider{position:absolute;left:161px;top:2046px;width:878px;height:1px;background:var(--line)}
.partners-title{position:absolute;left:0;width:1200px;top:2088px;text-align:center;font-size:22px;font-weight:400;color:#333;letter-spacing:.3px}
.partners{position:absolute;left:255px;top:2158px;width:720px;display:flex;justify-content:space-between;font-size:14px;color:#7a7a7a;font-weight:500}

/* footer */
.site-footer{position:absolute;left:0;top:2239px;width:1200px;height:122px;background:var(--footer)}
.share{position:absolute;left:161px;top:0;width:241px;height:122px;background:var(--red)}
.share .frame{position:absolute;left:6px;top:6px;right:6px;bottom:6px;border:1px dashed rgba(255,255,255,.7)}
.share h5{position:absolute;left:22px;top:40px;color:#fff;font-size:13px;font-weight:700;letter-spacing:.4px}
.share .nets{position:absolute;left:22px;top:72px;display:flex;gap:6px}
.share .nets span{background:#fff;color:var(--ink);font-size:9px;padding:3px 6px}
.contact{position:absolute;left:446px;top:20px;color:#fff}
.contact h5{font-size:13px;font-weight:700;letter-spacing:.4px}
.contact-cols{display:flex;gap:40px;margin-top:14px}
.contact p{font-size:10px;line-height:18px;color:#ccc;display:flex;gap:10px}
.contact p svg{flex:none;margin-top:4px}
.world{position:absolute;left:860px;top:10px;width:250px;height:100px;background:radial-gradient(ellipse at center,#3d3d3d 0%,#2f2f2f 70%)}
.bottom-bar{position:absolute;left:0;top:2361px;width:1200px;height:52px;background:var(--footer-bottom);color:#aaa;font-size:10px;text-align:center;line-height:52px}
</style>
</head>
<body>

<header class="site-header">
  <div class="brand">PENNIMO PAY</div>
  <div class="call">
    <span class="dot"><svg width="14" height="14" viewBox="0 0 24 24"><path fill="#d0202a" d="M6.6 10.8a15 15 0 0 0 6.6 6.6l2.2-2.2c.3-.3.7-.4 1-.2 1.1.4 2.3.6 3.6.6.6 0 1 .4 1 1V20c0 .6-.4 1-1 1A17 17 0 0 1 3 4c0-.6.4-1 1-1h3.5c.6 0 1 .4 1 1 0 1.3.2 2.5.6 3.6.1.3 0 .7-.2 1z"/></svg></span>
    CALL US: 0020-555-0147
  </div>
  <nav class="main-nav">
    <a class="active">HOME</a><a>ABOUT US</a><a>INTEGRATIONS</a><a>PRICEING</a><a>DOCUMENTATIONS</a><a class="u">SIGN UP</a><a class="u">LOGIN</a>
  </nav>
</header>

<section class="hero" role="img" aria-label="Evening photograph of a London bridge and riverside city lights">
  <h1>ABOUT</h1>
  <p>Sed ut perspiciatis unde omnis iste natus error sit voluptatem accusantium doloremque</p>
  <span class="hero-arrow prev"><svg width="16" height="20" viewBox="0 0 16 20"><path d="M12 2 4 10l8 8" fill="none" stroke="#fff" stroke-width="3"/></svg></span>
  <span class="hero-arrow next"><svg width="16" height="20" viewBox="0 0 16 20"><path d="m4 2 8 8-8 8" fill="none" stroke="#fff" stroke-width="3"/></svg></span>
</section>

<article class="feature" style="left:161px;top:510px;width:293px;height:320px;padding-top:18px">
  <div class="icon"><svg width="32" height="28" viewBox="0 0 32 28"><path d="M2 4h10l3 3h13v18H2z" fill="none" stroke="#d0202a" stroke-width="3"/><path d="M2 12h26" stroke="#d0202a" stroke-width="3"/></svg></div>
  <h3>OVERVIEW</h3>
  <div class="coins"><span>Varnel</span><span>Quorvath</span><span>Fembrisk</span></div>
  <ul class="ticks">
    <li>Micropayments</li>
    <li>Save your money</li>
    <li>Sell your product to anyone, anywhere</li>
    <li>End chargeback fraud an identity theft</li>
    <li>Exchange rates https://<a>ratefeedhub.example/</a></li>
  </ul>
</article>

<article class="feature" style="left:454px;top:465px;width:292px;height:365px;padding-top:25px;z-index:2">
  <div class="icon"><svg width="32" height="32" viewBox="0 0 32 32"><circle cx="13" cy="18" r="6" fill="none" stroke="#d0202a" stroke-width="4" stroke-dasharray="3 2"/><circle cx="13" cy="18" r="3" fill="#d0202a"/><circle cx="23" cy="9" r="4" fill="none" stroke="#d0202a" stroke-width="3" stroke-dasharray="2 2"/></svg></div>
  <h3>FEATURES</h3>
  <p>On the other hand, we denounce with righteous indignation and dislike men who are so beguiled and demoralized by the charms of moment...</p>
  <p style="margin-top:6px">Sed ut perspiciatis unde omnis iste natus error sit laudantium, totam rem aperiam, eaque ipsa architecto beatae vitae dicta sunt ratione voluptatem...</p>
  <div style="margin-top:16px"><span class="btn">CLICK VIEW MORE INFO!</span></div>
</article>

<article class="feature" style="left:746px;top:510px;width:293px;height:320px;padding-top:18px">
  <div class="icon"><svg width="30" height="30" viewBox="0 0 30 30"><rect x="4" y="6" width="18" height="18" fill="none" stroke="#d0202a" stroke-width="3"/><path d="M12 18l2-6 11-11 4 4-11 11z" fill="#fff" stroke="#d0202a" stroke-width="2.5"/></svg></div>
  <h3>ENTERPRICES</h3>
  <p>Sed ut perspiciatis unde omnis iste natus error sit voluptatem accusa lorentium doloremquit voluptatem accusantium dolore...</p>
  <p style="margin-top:6px">Sed ut perspiciatis unde omnis iste natus error sit beatae vitaeratione voluptatem...</p>
  <div style="margin-top:18px"><span class="btn">CLICK VIEW MORE INFO!</span></div>
</article>

<section class="integrations" role="img" aria-label="Dark dusk photograph of the London riverside skyline">
  <div class="section-title" style="top:38px;color:#fff"><span class="star">✱✱</span>INTEGRATIONS<span class="star">✱✱</span></div>
  <div class="coin-strip"><div><i></i>Varnel</div><div>Quorvath</div><div>Fembrisk</div></div>

  <div class="group" style="left:161px;top:250px">
    <div class="bar red"><b>‹</b>INTEGRATED SOLUTIONS<b>›</b></div>
    <div class="tiles"><span class="g">Paxtrel</span><span class="w">Quenvor</span><span class="w">Cartloom</span><span class="g">Trilvo</span></div>
  </div>
  <div class="group" style="left:454px;top:250px">
    <div class="bar dark"><b>‹</b>OPENSOURCE PLUGINS<b>›</b></div>
    <div class="tiles"><span class="g">Mervane</span><span class="w">Brindlecart</span><span class="w">Gatholm</span><span class="g">Crovinne</span></div>
  </div>
  <div class="group" style="left:746px;top:250px">
    <div class="bar red"><b>‹</b>POINT OF SALE<b>›</b></div>
    <div class="tiles"><span class="g">Paxtrel</span><span class="w">Mervane</span></div>
    <ul class="pos-notes">
      <li>Adipiscing elit, sed do eiusmod tempor incididunt ut labore et dolore magna aliqua...</li>
      <li>Adipiscing elit, sed do eiusmod tempor incididunt ut labore et dolore magna aliqua...</li>
    </ul>
  </div>

  <div class="group" style="left:161px;top:535px">
    <div class="bar red"><b>‹</b>BILLING AND ACCOUNTING<b>›</b></div>
    <div class="tiles"><span class="g">Holvaire</span><span class="w">Plenzo</span><span class="w">Nordquill</span><span class="g">Tallyvane</span></div>
  </div>
  <div class="group" style="left:454px;top:535px">
    <div class="bar dark"><b>‹</b>DONATIONS<b>›</b></div>
    <div class="tiles"><span class="g">Hopreth</span><span class="w">Spiremund</span><span class="w">Brevalia</span><span class="g">Orbenwell</span></div>
  </div>
  <div class="group" style="left:746px;top:535px">
    <div class="bar red"><b>‹</b>CODE LIBRARIES<b>›</b></div>
    <div class="tiles"><span class="g">Andrevo</span><span class="w">Cordlet</span><span class="w">Pomella</span><span class="g">Nodara</span></div>
  </div>
</section>

<div class="section-title" style="top:1754px;color:#333"><span class="star" style="color:#d0202a">●●</span>PRICEING<span class="star" style="color:#d0202a">●●</span></div>

<div class="plan red" style="left:161px">
  <h4>PACKAGE 1 - £349 P/M</h4>
  <ul><li>On the other hand, we denounce</li><li>At vero eos et accusamus et iusto odio</li><li>Sed ut perspiciatis unde omnis</li><li>Lorem ipsum dolor sit amet</li></ul>
  <svg class="fold" width="40" height="30" viewBox="0 0 40 30"><path d="M40 0v30H0z" fill="#333"/><path d="M26 22h10M31 17v10" stroke="#fff" stroke-width="2"/></svg>
</div>
<div class="plan dark" style="left:463px">
  <h4>PACKAGE 2 - £449 P/M</h4>
  <ul><li>On the other hand, we denounce</li><li>At vero eos et accusamus et iusto odio</li><li>Sed ut perspiciatis unde omnis</li><li>Lorem ipsum dolor sit amet</li></ul>
  <svg class="fold" width="40" height="30" viewBox="0 0 40 30"><path d="M40 0v30H0z" fill="#222"/><path d="M26 22h10M31 17v10" stroke="#fff" stroke-width="2"/></svg>
</div>
<div class="plan dark" style="left:766px">
  <h4>PACKAGE 3 - £749 P/M</h4>
  <ul><li>On the other hand, we denounce</li><li>At vero eos et accusamus et iusto odio</li><li>Sed ut perspiciatis unde omnis</li><li>Lorem ipsum dolor sit amet</li></ul>
  <svg class="fold" width="40" height="30" viewBox="0 0 40 30"><path d="M40 0v30H0z" fill="#222"/><path d="M26 22h10M31 17v10" stroke="#fff" stroke-width="2"/></svg>
</div>

<div class="divider"></div>
<h2 class="partners-title">OUR PARTNERS:UT PERSPICIATIS UNDE OMNIS IST</h2>
<div class="partners">
  <span>Ardent Cloud</span><span>Netrovia</span><span>Kestrin</span><span>Ovalund</span><span>Halbrook Systems</span><span>Iventrel</span><span>Marlowe Soft</span><span>Sorvani</span>
</div>

<footer class="site-footer">
  <div class="share"><div class="frame"></div>
    <h5>SHARE WITH US:</h5>
    <div class="nets"><span>Linkora</span><span>Friendra</span><span>Circlo</span><span>Chirpa</span></div>
  </div>
  <div class="world" role="img" aria-label="Faint world map"></div>
  <div class="contact">
    <h5>CONTACT US</h5>
    <div class="contact-cols">
      <div>
        <p><svg width="8" height="11" viewBox="0 0 8 11"><path d="M4 0a4 4 0 0 1 4 4c0 3-4 7-4 7S0 7 0 4a4 4 0 0 1 4-4z" fill="#ccc"/></svg><span>Our location 14 Harlow Lane 3/TOP097,<br>1220 Elmsford - lorem sipsm</span></p>
        <p style="margin-top:4px"><svg width="9" height="9" viewBox="0 0 24 24"><path fill="#ccc" d="M6.6 10.8a15 15 0 0 0 6.6 6.6l2.2-2.2c.3-.3.7-.4 1-.2 1.1.4 2.3.6 3.6.6.6 0 1 .4 1 1V20c0 .6-.4 1-1 1A17 17 0 0 1 3 4c0-.6.4-1 1-1h3.5c.6 0 1 .4 1 1 0 1.3.2 2.5.6 3.6.1.3 0 .7-.2 1z"/></svg>Phone: + 111 555 000</p>
      </div>
      <div style="margin-left:10px">
        <p><svg width="9" height="9" viewBox="0 0 9 9"><rect width="9" height="9" fill="#ccc"/></svg>Fax: + 111 555 001</p>
        <p style="margin-top:4px"><svg width="10" height="8" viewBox="0 0 10 8"><rect width="10" height="8" fill="#ccc"/><path d="M0 0l5 4 5-4" stroke="#2f2f2f" fill="none"/></svg>E-mail: hello@pennimopay.example</p>
      </div>
    </div>
  </div>
</footer>
<div class="bottom-bar">Copyright © 2015 &nbsp;Pennimo Pay. All Rights Reserved.Terms and conditions and Privacy Policy</div>

</body>
</html>
```